Online trading school - Website design

We are building an online trading school (trading of shares, commodities, indices, currencies). The purpose is to teach online traders how to trade successfully. We need to design the homepage of the website and logo (bramwelloq.com will be the domain). The homepage will contain the following elements

- logo
- Sign in and Register links/buttons
- upper menu
- short introduction
- a couple of bullet points 'Why to join our school?'
- sign up form
- text
- bottom menu

Attached is a draft for the designer. The draft is just for an inspiration, the actual structure of the website can be different if the designer thinks so.

The designer is free to choose colors.

School

3 page

```html
<!DOCTYPE html>
<html lang="en">
<head>
<meta charset="utf-8">
<title>Bramwelloq — Online Trading School</title>
<link href="https://fonts.googleapis.com/css2?family=Montserrat:wght@400;600;700&family=Open+Sans:wght@400;600;700&display=swap" rel="stylesheet">
<style>
  :root {
    --green: #8cb63c;
    --green-dark: #6f9429;
    --teal: #3bbfb1;
    --blue: #2fa0e0;
    --ink: #2b2b2b;
    --text: #555;
    --light: #f2f2f2;
    --white: #fff;
  }
  * { margin: 0; padding: 0; box-sizing: border-box; }
  html, body { width: 1200px; height: 3000px; overflow: hidden; }
  body { font-family: "Open Sans", Arial, sans-serif; color: var(--text); background: var(--white); position: relative; }
  .heading { font-family: "Montserrat", Arial, sans-serif; font-weight: 700; letter-spacing: 1px; }
  .btn { display: inline-block; background: var(--green); color: var(--white); font-family: "Montserrat", Arial, sans-serif; font-weight: 600; font-size: 14px; padding: 11px 20px; letter-spacing: .5px; }
  .btn-ghost { background: transparent; border: 2px solid var(--green); }

  /* hero */
  .hero { position: absolute; left: 0; top: 0; width: 1200px; height: 700px; background: linear-gradient(135deg, #3a3f44 0%, #23272b 45%, #4a4640 100%); }
  .hero-photo { position: absolute; inset: 0; background: radial-gradient(circle at 30% 40%, rgba(120,110,95,.45), transparent 60%), radial-gradient(circle at 80% 70%, rgba(90,100,110,.4), transparent 55%); }
  .topbar { position: absolute; top: 0; left: 140px; width: 920px; height: 64px; display: flex; align-items: center; justify-content: space-between; }
  .logo { display: flex; align-items: center; gap: 10px; }
  .logo-dot { width: 34px; height: 34px; border-radius: 50%; background: var(--green); }
  .logo-name { font-family: "Montserrat", Arial, sans-serif; font-weight: 700; font-size: 32px; color: var(--white); }
  .account { display: flex; align-items: center; gap: 14px; color: var(--white); font-size: 14px; font-weight: 700; }
  .account .sep { opacity: .6; }
  .social { display: flex; gap: 10px; margin-left: 8px; }
  .social span { width: 18px; height: 18px; background: var(--white); border-radius: 2px; }
  .nav { position: absolute; top: 100px; left: 140px; width: 920px; height: 40px; display: flex; gap: 6px; border-bottom: 1px solid rgba(255,255,255,.25); }
  .nav a { color: var(--white); font-family: "Montserrat", Arial, sans-serif; font-size: 15px; font-weight: 600; padding: 10px 16px; text-decoration: none; }
  .nav a.active { background: var(--green); }
  .hero-copy { position: absolute; top: 240px; left: 140px; width: 560px; color: var(--white); }
  .hero-copy .eyebrow { font-size: 30px; font-family: "Montserrat", Arial, sans-serif; font-weight: 600; letter-spacing: 1px; }
  .hero-copy h1 { font-size: 56px; margin-top: 4px; }
  .hero-copy p { font-size: 18px; margin-top: 18px; line-height: 1.4; width: 460px; }
  .hero-actions { margin-top: 70px; display: flex; gap: 40px; }

  .join { position: absolute; top: 230px; left: 760px; width: 296px; height: 330px; background: var(--white); padding: 22px; box-shadow: 0 6px 20px rgba(0,0,0,.35); }
  .join h2 { font-size: 16px; color: var(--ink); padding-bottom: 10px; border-bottom: 1px solid #ddd; }
  .field { height: 40px; border: 1px solid #ddd; margin-top: 14px; font-size: 13px; color: #aaa; padding: 11px 12px; }
  .agree { display: flex; align-items: center; gap: 8px; font-size: 11px; margin-top: 14px; }
  .agree span.box { width: 12px; height: 12px; border: 1px solid #aaa; }
  .join .btn { display: block; text-align: center; margin-top: 16px; }

  /* market cards */
  .markets { position: absolute; top: 620px; left: 140px; width: 920px; height: 190px; display: flex; gap: 8px; }
  .card { flex: 1; display: flex; flex-direction: column; align-items: center; padding-top: 28px; color: var(--white); box-shadow: 0 4px 12px rgba(0,0,0,.15); }
  .card svg { width: 54px; height: 54px; }
  .card h3 { font-size: 18px; margin-top: 12px; font-family: "Montserrat", Arial, sans-serif; }
  .card .more { margin-top: 18px; font-size: 11px; border: 1px solid currentColor; padding: 4px 14px; font-weight: 600; }
  .card.shares { background: var(--white); color: var(--blue); }
  .card.commodities { background: var(--teal); }
  .card.indices { background: var(--green); }
  .card.currencies { background: var(--blue); }

  /* intro */
  .intro { position: absolute; top: 810px; left: 0; width: 1200px; height: 470px; background: var(--light); }
  .section-inner { position: absolute; left: 140px; width: 920px; }
  .intro .section-inner { top: 100px; }
  .title { font-size: 38px; color: var(--ink); }
  .rule { width: 80px; height: 5px; background: var(--green); margin: 12px 0 26px; }
  .body-text { font-size: 17px; line-height: 1.6; }
  .section-inner .btn { margin-top: 30px; }

  /* progress */
  .progress { position: absolute; top: 1280px; left: 0; width: 1200px; height: 440px; background: linear-gradient(180deg, #2a2522 0%, #1b1d20 100%); }
  .progress-photo { position: absolute; inset: 0; background: radial-gradient(circle at 25% 60%, rgba(150,120,90,.35), transparent 55%); }
  .progress h2 { position: absolute; top: 80px; width: 100%; text-align: center; color: var(--green); font-size: 40px; }
  .gauges { position: absolute; top: 180px; left: 140px; width: 920px; display: flex; justify-content: space-around; }
  .gauge { text-align: center; color: var(--white); }
  .gauge svg { width: 130px; height: 130px; }
  .gauge .label { font-size: 16px; font-weight: 700; margin-top: 16px; letter-spacing: .5px; }

  /* why */
  .why { position: absolute; top: 1720px; left: 0; width: 1200px; height: 480px; background: var(--light); }
  .why .section-inner { top: 70px; }
  .why .title { color: var(--green-dark); }
  .reasons { list-style: none; }
  .reasons li { display: flex; align-items: center; gap: 16px; font-size: 20px; font-weight: 700; color: var(--ink); margin-bottom: 20px; }
  .reasons svg { width: 30px; height: 30px; flex: none; }
  .why-photo { position: absolute; top: 1860px; left: 620px; width: 440px; height: 290px; background: linear-gradient(135deg, #dfe4ea 0%, #4b5d73 55%, #2c3440 100%); }

  /* offer */
  .offer { position: absolute; top: 2200px; left: 0; width: 1200px; height: 400px; background: linear-gradient(180deg, #2e3033 0%, #1c1e21 100%); }
  .offer .section-inner { top: 60px; }
  .offer .title { color: var(--green); }
  .offer .body-text { color: var(--white); }

  /* contact */
  .contact { position: absolute; top: 2600px; left: 0; width: 1200px; height: 360px; background: linear-gradient(180deg, #35402a 0%, #2b3424 100%); }
  .contact h2 { position: absolute; top: 60px; width: 100%; text-align: center; color: var(--green); font-size: 40px; }
  .contact .rule { position: absolute; top: 118px; left: 560px; margin: 0; }
  .contact-items { position: absolute; top: 170px; left: 140px; width: 920px; display: flex; justify-content: space-between; }
  .contact-item { width: 280px; text-align: center; color: var(--white); }
  .contact-item svg { width: 84px; height: 84px; }
  .contact-item .label { font-size: 14px; font-weight: 700; margin-top: 12px; }
  .contact-item .value { font-size: 14px; margin-top: 6px; opacity: .85; }

  .footer { position: absolute; top: 2960px; left: 0; width: 1200px; height: 40px; background: var(--green); color: var(--white); font-size: 13px; font-weight: 600; }
  .footer .section-inner { top: 11px; display: flex; justify-content: space-between; }
  .footer .links { display: flex; gap: 24px; }
</style>
</head>
<body>

<header class="hero">
  <div class="hero-photo" role="img" aria-label="Dark photo of a trader's desk with laptop and notebook"></div>
  <div class="topbar">
    <div class="logo"><span class="logo-dot"></span><span class="logo-name">Bramwelloq</span></div>
    <div class="account">
      <span>SIGNUP</span><span class="sep">|</span><span>LOGIN</span><span class="sep">|</span>
      <div class="social"><span></span><span></span><span></span><span></span></div>
    </div>
  </div>
  <nav class="nav">
    <a class="active">HOME</a><a>ABOUT OUR SCHOOL</a><a>RISK WARNING</a><a>FAQ</a><a>TRADING GLOSSARY</a><a>CONTACT</a>
  </nav>
  <div class="hero-copy">
    <div class="eyebrow">EXPERIENCE, EXPERTISE &amp;</div>
    <h1 class="heading">BUSINESS SAVVY</h1>
    <p>Lorem Ipsum has been the industry's standard dummy text ever since the 1500s.</p>
    <div class="hero-actions"><span class="btn">OUR BENEFITS</span><span class="btn btn-ghost">VIRTUAL TOUR</span></div>
  </div>
  <form class="join">
    <h2 class="heading">JOIN OUR SCHOOL</h2>
    <div class="field">Name</div>
    <div class="field">Email</div>
    <div class="field">Phone</div>
    <div class="agree"><span class="box"></span>I agree with the terms and conditions</div>
    <span class="btn">CLICK HERE</span>
  </form>
</header>

<section class="markets">
  <div class="card shares">
    <svg viewBox="0 0 54 54" fill="none" stroke="currentColor" stroke-width="3"><path d="M6 46h42M12 40V30M22 40V22M32 40V28M42 40V14M10 26l12-10 10 8 12-14"/></svg>
    <h3>Trading of Shares</h3><span class="more">READ MORE</span>
  </div>
  <div class="card commodities">
    <svg viewBox="0 0 54 54" fill="none" stroke="currentColor" stroke-width="3"><path d="M8 20h38l-4 26H12z M18 20a9 9 0 0 1 18 0"/></svg>
    <h3>Commodities</h3><span class="more">READ MORE</span>
  </div>
  <div class="card indices">
    <svg viewBox="0 0 54 54" fill="none" stroke="currentColor" stroke-width="3"><path d="M8 8v38h40M14 36l10-12 8 6 12-16"/></svg>
    <h3>Indices</h3><span class="more">READ MORE</span>
  </div>
  <div class="card currencies">
    <svg viewBox="0 0 54 54" fill="none" stroke="currentColor" stroke-width="4"><path d="M27 6v42M36 16c-2-4-16-5-17 3s18 7 18 15-16 8-19 2"/></svg>
    <h3>Currencies</h3><span class="more">READ MORE</span>
  </div>
</section>

<section class="intro">
  <div class="section-inner">
    <h2 class="heading title">INTRODUCTION</h2>
    <div class="rule"></div>
    <p class="body-text">Lorem Ipsum has been the industry's standard dummy text ever since the 1500s, when an unknown printer took a galley of type and scrambled it to make a type specimen book. It has survived not only five centuries, but also the leap into electronic typesetting, remaining essentially unchanged. It was popularised in the 1960s with the release of printed transfer sheets containing Lorem Ipsum passages, and more recently with modern layout tools and desktop publishing software including versions of Lorem Ipsum.</p>
    <span class="btn">LEARN MORE</span>
  </div>
</section>

<section class="progress">
  <div class="progress-photo" role="img" aria-label="Dimmed photo of hands typing on a laptop"></div>
  <h2 class="heading">PROGRESS BARS</h2>
  <div class="gauges">
    <div class="gauge">
      <svg viewBox="0 0 130 130"><circle cx="65" cy="65" r="55" fill="none" stroke="rgba(255,255,255,.15)" stroke-width="6"/><circle cx="65" cy="65" r="55" fill="none" stroke="#8cb63c" stroke-width="6" stroke-dasharray="172.8 345.6" transform="rotate(-90 65 65)"/><text x="65" y="73" text-anchor="middle" fill="#fff" font-size="24" font-family="Open Sans, sans-serif" font-weight="600">50%</text></svg>
      <div class="label">TRADING OF SHARES</div>
    </div>
    <div class="gauge">
      <svg viewBox="0 0 130 130"><circle cx="65" cy="65" r="55" fill="none" stroke="rgba(255,255,255,.15)" stroke-width="6"/><circle cx="65" cy="65" r="55" fill="none" stroke="#8cb63c" stroke-width="6" stroke-dasharray="259.2 345.6" transform="rotate(-90 65 65)"/><text x="65" y="73" text-anchor="middle" fill="#fff" font-size="24" font-family="Open Sans, sans-serif" font-weight="600">75%</text></svg>
      <div class="label">COMMODITIES</div>
    </div>
    <div class="gauge">
      <svg viewBox="0 0 130 130"><circle cx="65" cy="65" r="55" fill="none" stroke="rgba(255,255,255,.15)" stroke-width="6"/><circle cx="65" cy="65" r="55" fill="none" stroke="#8cb63c" stroke-width="6" stroke-dasharray="293.8 345.6" transform="rotate(-90 65 65)"/><text x="65" y="73" text-anchor="middle" fill="#fff" font-size="24" font-family="Open Sans, sans-serif" font-weight="600">85%</text></svg>
      <div class="label">INDICES</div>
    </div>
    <div class="gauge">
      <svg viewBox="0 0 130 130"><circle cx="65" cy="65" r="55" fill="none" stroke="#8cb63c" stroke-width="6"/><text x="65" y="73" text-anchor="middle" fill="#fff" font-size="24" font-family="Open Sans, sans-serif" font-weight="600">100%</text></svg>
      <div class="label">CURRENCIES</div>
    </div>
  </div>
</section>

<section class="why">
  <div class="section-inner">
    <h2 class="heading title">WHY TO JOIN US?</h2>
    <div class="rule"></div>
    <ul class="reasons">
      <li><svg viewBox="0 0 30 30"><circle cx="15" cy="15" r="14" fill="#8cb63c"/><path d="M8 15l5 5 9-10" fill="none" stroke="#fff" stroke-width="3"/></svg>Best Trading Tips Ever.</li>
      <li><svg viewBox="0 0 30 30"><circle cx="15" cy="15" r="14" fill="#8cb63c"/><path d="M8 15l5 5 9-10" fill="none" stroke="#fff" stroke-width="3"/></svg>Secret Tips from Experts.</li>
      <li><svg viewBox="0 0 30 30"><circle cx="15" cy="15" r="14" fill="#8cb63c"/><path d="M8 15l5 5 9-10" fill="none" stroke="#fff" stroke-width="3"/></svg>We Teach you how to Trade Online.</li>
      <li><svg viewBox="0 0 30 30"><circle cx="15" cy="15" r="14" fill="#8cb63c"/><path d="M8 15l5 5 9-10" fill="none" stroke="#fff" stroke-width="3"/></svg>Learn how to Trade commodities.</li>
      <li><svg viewBox="0 0 30 30"><circle cx="15" cy="15" r="14" fill="#8cb63c"/><path d="M8 15l5 5 9-10" fill="none" stroke="#fff" stroke-width="3"/></svg>Learn how to become a Trader.</li>
    </ul>
  </div>
</section>
<div class="why-photo" role="img" aria-label="Photo of three smiling business people in suits"></div>

<section class="offer">
  <div class="section-inner">
    <h2 class="heading title">WHAT DO WE OFFER?</h2>
    <div class="rule"></div>
    <p class="body-text">Lorem Ipsum has been the industry's standard dummy text ever since the 1500s, when an unknown printer took a galley of type and scrambled it to make a type specimen book. It has survived not only five centuries, but also the leap into electronic typesetting, remaining essentially unchanged. It was popularised in the 1960s with the release of printed transfer sheets containing Lorem Ipsum passages, and more recently with modern layout tools and desktop publishing software including versions of Lorem Ipsum.</p>
    <span class="btn">LEARN MORE</span>
  </div>
</section>

<section class="contact">
  <h2 class="heading">CONTACT US</h2>
  <div class="rule"></div>
  <div class="contact-items">
    <div class="contact-item">
      <svg viewBox="0 0 84 84"><circle cx="42" cy="42" r="40" fill="#8cb63c"/><path d="M42 24a11 11 0 0 0-11 11c0 9 11 22 11 22s11-13 11-22a11 11 0 0 0-11-11z" fill="#fff"/><circle cx="42" cy="35" r="4" fill="#8cb63c"/></svg>
      <div class="label">ADDRESS</div><div class="value">27 Orchard Row, Calden 40418</div>
    </div>
    <div class="contact-item">
      <svg viewBox="0 0 84 84"><circle cx="42" cy="42" r="40" fill="#8cb63c"/><path d="M30 26c3-2 6 0 8 4s1 6-1 7c1 4 5 8 9 9 1-2 3-3 7-1s6 5 4 8c-3 4-10 4-18-4s-12-16-9-23z" fill="#fff"/></svg>
      <div class="label">PHONE</div><div class="value">+000 234 5678 910</div>
    </div>
    <div class="contact-item">
      <svg viewBox="0 0 84 84"><circle cx="42" cy="42" r="40" fill="#8cb63c"/><rect x="26" y="30" width="32" height="24" fill="#fff"/><path d="M26 30l16 13 16-13" fill="none" stroke="#8cb63c" stroke-width="2.5"/></svg>
      <div class="label">EMAIL</div><div class="value">support@bramwelloq.com</div>
    </div>
  </div>
</section>

<footer class="footer">
  <div class="section-inner">
    <span>© 2024 Online Trading School. All rights reserved</span>
    <div class="links"><span>TERMS &amp; CONDITIONS</span><span>PRIVACY POLICY</span></div>
  </div>
</footer>

</body>
</html>
```